Retail and Ecommerce Archery Shop needs new Home Page Design

We need a homepage design created for an existing company named Redhollow Bowsport Hub. They sell various types of Archery equipment for both Bow hunting and Target shooting both in store and online. They offer shooting lessons, have an indoor archery shooting range with memberships available, and have their own line of bowstrings. For color scheme, use the current home page as inspiration. The Homepage Template has links to specific images, if any other images are needed, stock images are acceptable.

Current Website: https://rhbowsporthub.com/

Customer Avatar: https://files.quillnest.net/page/d/4Tq8Wm2RbXk9LpZ3vNc7HyF1gJd6sKe5uA0oVtB2/view?mode=shared

Core Message Canvas: https://files.quillnest.net/tables/d/7Hm_482rTz906R3k21wLuNy8Pq0Zc47bd5jS2X_vW/view?mode=shared

Homepage Template-Use this worksheet as the structue of the homepage: https://files.quillnest.net/page/d/9xkpWvRfa2B5nT7eLcM3JsYq0HdG8oUiZbN4/view?mode=shared

```html
<!DOCTYPE html>
<html lang="en">
<head>
<meta charset="utf-8">
<title>Redhollow Bowsport Hub – Home</title>
<link href="https://fonts.googleapis.com/css2?family=Cinzel:wght@600;700&family=Jost:wght@400;500;600&display=swap" rel="stylesheet">
<style>
:root{
  --bg:#121212;
  --bg-deep:#0b0b0b;
  --bar:#1a1a1a;
  --band:#1d1d1d;
  --panel:#2a2a2a;
  --yellow:#f5d10f;
  --red:#e11a22;
  --blue:#0a8ad0;
  --white:#ffffff;
  --muted:#cfcfcf;
  --faint:rgba(255,255,255,0.03);
}
*{margin:0;padding:0;box-sizing:border-box}
html,body{width:1200px;height:3881px;overflow:hidden;background:var(--bg);color:var(--white);font-family:'Jost',sans-serif}
.page{position:relative;width:1200px;height:3881px;overflow:hidden}
.abs{position:absolute}
.serif{font-family:'Cinzel',serif;font-weight:700;text-transform:uppercase}
.btn{position:absolute;display:flex;align-items:center;justify-content:center;border-radius:16px;font-size:8px;font-weight:600;letter-spacing:3px;text-transform:uppercase}
.btn-yellow{background:var(--yellow);color:#111}
.btn-red{background:var(--red);color:#fff}
.rule{position:absolute;height:2px;background:#8a7a22}
.watermark{position:absolute;font-family:'Cinzel',serif;font-weight:700;font-size:130px;color:var(--faint);letter-spacing:4px;white-space:nowrap}

/* header */
.site-header{position:absolute;left:0;top:0;width:1200px;height:119px;z-index:5}
.top-strip{left:0;top:0;width:1200px;height:45px;background:var(--bg-deep)}
.nav-bar{left:0;top:45px;width:1200px;height:74px;background:var(--bar)}
.search{left:197px;top:13px;display:flex;align-items:center;gap:18px;font-size:8px;color:var(--muted)}
.icon-dot{width:20px;height:20px;border-radius:50%;background:var(--yellow);display:flex;align-items:center;justify-content:center}
.cart{left:982px;top:12px}
.nav-link{position:absolute;top:72px;font-size:12px;color:var(--white);text-decoration:none;letter-spacing:.5px}
.brand{left:470px;top:38px;width:260px;text-align:center;font-family:'Cinzel',serif;font-weight:700;color:var(--yellow);font-size:22px;line-height:24px}

/* hero */
.hero-photo{left:0;top:119px;width:1200px;height:816px;background:linear-gradient(180deg,#2c2a24 0%,#3a3428 35%,#1f1d19 70%,var(--bg) 100%)}
.hero-title{position:absolute;left:197px;top:686px;font-size:46px;line-height:53px;letter-spacing:1px;white-space:nowrap}
.hero-line{left:197px;top:800px;width:200px;height:2px;background:#8a7a22}
.hero-tag{left:197px;top:823px;font-size:13px;letter-spacing:.3px}
.scroll{left:910px;top:765px}

/* about */
.about-img{left:197px;top:1019px;width:412px;height:461px;background:linear-gradient(160deg,#8a8a32,#4a4a22 45%,#2e2a1e)}
.about-title{position:absolute;left:659px;top:1088px;font-size:33px;line-height:41px}
.about-copy{position:absolute;left:659px;top:1245px;width:340px;font-size:13px;line-height:20px}

/* logos */
.logos{left:0;top:1602px;width:1200px;height:166px;background:var(--band)}
.logo-shape{position:absolute;top:62px;height:40px;background:#3a3a3a}

/* video */
.video-img{left:496px;top:1907px;width:506px;height:351px;background:linear-gradient(90deg,#6f6a62,#a8a39a 40%,#7a2a2a 70%,#cfcac2)}
.video-title{position:absolute;left:197px;top:2010px;font-size:33px;line-height:40px}

/* features */
.features-bg{left:0;top:2700px;width:1200px;height:440px;background:linear-gradient(180deg,var(--bg) 0%,#262626 40%,#1e1e1e 70%,var(--bg) 100%)}
.features-title{position:absolute;left:0;width:1200px;top:2445px;text-align:center;font-size:45px;line-height:52px}
.features-sub{position:absolute;left:0;width:1200px;top:2584px;text-align:center;font-size:12px;letter-spacing:.5px}
.card{position:absolute;top:2653px;width:256px;height:290px;background:linear-gradient(180deg,#4a4a4a,#3a3a3a);border-radius:6px;padding:38px 34px 0}
.card .num{position:absolute;right:24px;top:-32px;font-family:'Cinzel',serif;font-weight:700;font-size:66px;color:var(--yellow);line-height:70px}
.card h3{font-size:11px;font-weight:500;line-height:18px;text-transform:uppercase;height:62px;border-bottom:1px solid #6a6a6a;margin-bottom:18px;padding-bottom:6px}
.card p{font-size:9px;line-height:14px;color:#e6e6e6}

/* newsletter */
.news{left:133px;top:3154px;width:933px;height:241px;background:var(--blue);border-radius:4px}
.news h2{position:absolute;left:64px;top:40px;font-size:32px;line-height:42px}
.news .lead{position:absolute;left:64px;top:166px;font-size:12px;line-height:16px;text-transform:uppercase;color:var(--yellow)}
.news .intro{position:absolute;left:508px;top:48px;font-size:10px;line-height:15px}
.news .field{position:absolute;left:508px;top:106px;width:362px;height:38px;border:1.5px solid #fff;border-radius:20px;font-size:9px;padding:12px 26px}
.news .sub-btn{position:absolute;left:508px;top:158px;width:237px;height:30px;background:#fff;color:#111;border-radius:16px;display:flex;align-items:center;justify-content:center;font-size:8px;font-weight:600;letter-spacing:3px}

/* footer */
.footer-brand{left:197px;top:3530px;font-family:'Cinzel',serif;font-weight:700;color:var(--yellow);font-size:24px;line-height:27px;width:230px}
.footer-about{left:197px;top:3645px;width:230px;font-size:9px;line-height:15px;color:var(--muted)}
.social{top:3717px;width:26px;height:26px;border-radius:50%;background:var(--red)}
.flink{position:absolute;left:519px;font-size:9px;color:var(--white);text-decoration:none;text-transform:uppercase}
.contact{left:725px;top:3508px;width:277px;height:243px;background:var(--panel)}
.c-item{position:absolute;left:64px;font-size:9px;line-height:13px}
.c-item small{display:block;font-size:6px;color:var(--muted);letter-spacing:.5px}
.c-icon{position:absolute;left:32px}
.bottom{left:0;top:3837px;width:1200px;height:44px;background:var(--bar);font-size:9px}
</style>
</head>
<body>
<div class="page">

  <!-- hero -->
  <div class="abs hero-photo" role="img" aria-label="Bow hunter in camouflage drawing a compound bow in a forest"></div>
  <h1 class="serif hero-title">Your Bow Hunting<br>Adventure Starts Here!</h1>
  <div class="abs hero-line"></div>
  <div class="abs hero-tag">TOP-NOTCH EQUIPMENT - EXPERTISE - UNMATCHED SUPPORT</div>
  <div class="btn btn-yellow" style="left:197px;top:868px;width:225px;height:30px">Indoor Archery Range</div>
  <div class="btn btn-red" style="left:435px;top:868px;width:225px;height:30px">Shop Our Bows</div>
  <svg class="abs scroll" width="100" height="140" viewBox="0 0 100 140">
    <path id="arcS" d="M12 50 A38 38 0 0 1 88 50" fill="none"/>
    <text font-family="Jost" font-size="8" fill="#fff" letter-spacing="6"><textPath href="#arcS">SCROLL DOWN</textPath></text>
    <circle cx="50" cy="56" r="3" fill="#e11a22"/>
    <line x1="50" y1="64" x2="50" y2="135" stroke="#777" stroke-width="1"/>
  </svg>

  <!-- header -->
  <header class="site-header">
    <div class="abs top-strip"></div>
    <div class="abs nav-bar"></div>
    <svg class="abs" style="left:450px;top:0" width="300" height="45"><path d="M0 0H300L280 45H20Z" fill="#1a1a1a"/></svg>
    <div class="abs search">SEARCH...<span class="icon-dot"><svg width="10" height="10" viewBox="0 0 10 10"><circle cx="4" cy="4" r="3" fill="none" stroke="#111" stroke-width="1.5"/><path d="M6.3 6.3L9 9" stroke="#111" stroke-width="1.5"/></svg></span></div>
    <div class="abs cart icon-dot"><svg width="10" height="10" viewBox="0 0 10 10"><path d="M1 2h1.5l1 5h4.5l1-3.5H3" fill="none" stroke="#111" stroke-width="1.2"/></svg></div>
    <nav>
      <a class="nav-link" style="left:197px">SHOP</a>
      <a class="nav-link" style="left:274px">ABOUT US</a>
      <a class="nav-link" style="left:378px">RANGE</a>
      <a class="nav-link" style="left:758px">PRO SHOP</a>
      <a class="nav-link" style="left:864px">ELECTRIC BOWSTRINGS</a>
    </nav>
    <div class="abs brand">Redhollow<br>Bowsport Hub</div>
  </header>

  <!-- about -->
  <div class="watermark" style="left:20px;top:940px">REDHOLLOW</div>
  <div class="watermark" style="left:590px;top:1520px">ABOUT</div>
  <div class="abs about-img" role="img" aria-label="Young archer in camouflage holding a compound bow among autumn trees"></div>
  <h2 class="serif about-title">We Are A Full-<br>Service Archery<br>Pro Shop</h2>
  <div class="rule" style="left:659px;top:1210px;width:180px"></div>
  <p class="about-copy">Our Services Include Bow Setup And Sizing, D-Loop And Peep Sight Installs, Accessory Installs, And Setup, Cam/Limb Swaps, String Swaps, Paper Tuning, 2nd/3rd Axis Adjustments, Replacement Parts, Arrow Building, Tuning, And Much More!</p>
  <div class="btn btn-yellow" style="left:659px;top:1373px;width:141px;height:30px">Shop Now</div>

  <!-- partner logos -->
  <div class="abs logos">
    <div class="logo-shape" style="left:78px;width:92px;background:#5a2222"></div>
    <div class="logo-shape" style="left:263px;width:92px;border-radius:50%;background:#4a4322"></div>
    <div class="logo-shape" style="left:448px;width:100px"></div>
    <div class="logo-shape" style="left:636px;width:128px;height:24px;top:70px"></div>
    <div class="logo-shape" style="left:846px;width:110px"></div>
    <div class="logo-shape" style="left:1060px;top:56px;width:40px;height:40px;border-radius:50%;background:#23456a"></div>
  </div>

  <!-- video -->
  <div class="watermark" style="left:740px;top:1820px">VIDEO</div>
  <div class="abs video-img" role="img" aria-label="Close-up of a red bowstring serving machine winding a custom string"></div>
  <h2 class="serif video-title">Our Custom<br>Electric<br>Bowstrings</h2>
  <div class="rule" style="left:197px;top:2145px;width:163px"></div>
  <svg class="abs" style="left:432px;top:2203px" width="110" height="110" viewBox="0 0 110 110">
    <path id="arcP" d="M55 15 A40 40 0 1 1 54.9 15" fill="none"/>
    <text font-family="Jost" font-size="7" fill="#fff" letter-spacing="3"><textPath href="#arcP">CLICK PLAY TO START &amp; STOP</textPath></text>
    <circle cx="55" cy="55" r="29" fill="#fff"/>
    <path d="M49 44L66 55L49 66Z" fill="#e11a22"/>
  </svg>

  <!-- features -->
  <div class="abs features-bg" role="img" aria-label="Dark silhouette of an archer against a mountain landscape"></div>
  <div class="watermark" style="left:250px;top:2350px">FEATURES</div>
  <h2 class="serif features-title">Welcome To Your Local<br>Archery Shop</h2>
  <div class="rule" style="left:518px;top:2558px;width:164px"></div>
  <div class="features-sub">WHERE CONSISTENCY IS BUILT</div>
  <div class="card" style="left:197px">
    <div class="num">01</div>
    <h3>Looking For A New Bow Setup?</h3>
    <p>Our custom bow-fitting process will be perfect for you. We get you set up the right way, the first time! We will get your measurements, check your shot, and make sure you leave feeling confident with your new Bow!</p>
  </div>
  <div class="card" style="left:472px">
    <div class="num">02</div>
    <h3>Looking To Make Some Improvements To Your Current Archery Setup?</h3>
    <p>We have access to almost all of the popular archery accessories on the market! We don't sell anything we wouldn't use ourselves so come on in and talk with our shop experts to figure out what will work best for you.</p>
  </div>
  <div class="card" style="left:746px">
    <div class="num">03</div>
    <h3>Are You Looking To Improve Your Shot? Reserve Some Time On Our Range!</h3>
    <p>Before you step into the field to take your first shot of the season, take time to go to the range. Archery, like any skill, requires practice &amp; diligence to develop a consistent &amp; confident shot. We have a 12-lane 20-yard indoor range in the shop. Daily Range and memberships are available. We also offer bow rental and lessons</p>
  </div>
  <div class="btn btn-red" style="left:488px;top:3000px;width:224px;height:31px">Range Informaiton</div>

  <!-- newsletter -->
  <div class="watermark" style="left:0;top:3070px">NEWSLETTER</div>
  <section class="abs news">
    <h2 class="serif">Join Our Archery<br>Community</h2>
    <div class="lead">Exclusive Deals, Tips, And Updates<br>Straight To Your Inbox!</div>
    <div class="intro">Join Today &amp; Stay Up-To-Date On New Product Releases, Shop<br>Promotions, And Our Archery Newsletters</div>
    <div class="field">Email</div>
    <div class="sub-btn">SUBSCRIBE OUR NEWSLETTER</div>
  </section>

  <!-- footer -->
  <div class="abs footer-brand">Redhollow<br>Bowsport Hub</div>
  <div class="abs footer-about">Lorem Ipsum is simply dummy text of the printing and typesetting industry. Lorem Ipsum has been the industry's standard dummy text ever since the 1500s.</div>
  <div class="abs social" style="left:199px"></div>
  <div class="abs social" style="left:239px"></div>
  <nav>
    <a class="flink" style="top:3545px">Shop</a>
    <a class="flink" style="top:3590px">About Us</a>
    <a class="flink" style="top:3635px">Range</a>
    <a class="flink" style="top:3680px">Pro Shop</a>
    <a class="flink" style="top:3725px">Electric Bowstrings</a>
  </nav>
  <div class="abs contact">
    <svg class="c-icon" style="top:38px" width="14" height="11" viewBox="0 0 14 11"><rect x="0.5" y="0.5" width="13" height="10" fill="#fff"/><path d="M0.5 0.5L7 6L13.5 0.5" fill="none" stroke="#2a2a2a"/></svg>
    <div class="c-item" style="top:32px"><small>MAIL</small>hello@rhbowsporthub.com</div>
    <svg class="c-icon" style="top:98px" width="14" height="14" viewBox="0 0 14 14"><path d="M13 1L1 6l5 2 2 5z" fill="#fff"/></svg>
    <div class="c-item" style="top:92px"><small>ADDRESS</small>Unit 4, Fernbrook Trade Park<br>18 Alder Lane, Redhollow<br>RH4 2QT</div>
    <svg class="c-icon" style="top:182px" width="14" height="14" viewBox="0 0 14 14"><path d="M3 1l3 3-2 2c1 2 2 3 4 4l2-2 3 3-2 2C6 13 1 8 1 3z" fill="#fff"/></svg>
    <div class="c-item" style="top:182px"><small>PHONE</small>+44 (0)120 555 0148</div>
  </div>
  <div class="abs bottom">
    <div class="abs" style="left:197px;top:16px">© Copyright © 2023 Alderpoint Studio. All Rights Reserved.</div>
    <div class="abs" style="left:840px;top:16px">Terms Of Service &nbsp;&nbsp;|&nbsp;&nbsp; Privacy Policy</div>
  </div>
</div>
</body>
</html>
```